Verodex business card

Business card for sustainable investment company called "Verodex". Verodex is an exchange platform selling carbon credits between buyers and sellers. Carbon Credits are an environmental commodity for reducing global carbon emissions.

the card should obviously have our logo and the theme should be sustainability/environment mixed with a trading platform.

Contact Information for Business Card

Logo, Name, Title, Phone, Email

Colors
0054AA
0677BA
7BADD7
CADEEF
E8F1F8
0094D4
00A9DD
6FCCEA
C7EBF8
E9F6FB
00AB8E
00BBA5
67D7C9
C6EFE9
E9F9F6
59FF00
82FF00
B8FF75
E3FFCB
F4FFEA

```html
<!DOCTYPE html>
<html lang="en">
<head>
<meta charset="utf-8">
<title>Verodex business card</title>
<link rel="stylesheet" href="https://fonts.googleapis.com/css2?family=Raleway:wght@700&family=Lato:wght@400;700&display=swap">
<style>
  :root {
    --page-bg: #e9f6fb;
    --card-white: #ffffff;
    --navy: #1f3350;
    --band: #0054aa;
    --wedge: #c6efe9;
    --teal: #00ab8e;
    --lime: #82ff00;
    --gradient-start: #00bba5;
    --gradient-mid: #0094d4;
    --gradient-end: #0054aa;
    --text-light: #ffffff;
    --icon-detail: #0677ba;
  }
  * { margin: 0; padding: 0; box-sizing: border-box; }
  html, body {
    width: 1200px;
    height: 1200px;
    overflow: hidden;
    background: var(--page-bg);
  }
  .canvas { position: relative; width: 1200px; height: 1200px; }

  .card {
    position: absolute;
    left: 161px;
    width: 877px;
    height: 513px;
    overflow: hidden;
  }
  .card--front { top: 62px; background: var(--card-white); }
  .card--back {
    top: 614px;
    background: linear-gradient(90deg, var(--gradient-start), var(--gradient-mid) 55%, var(--gradient-end));
    display: flex;
    align-items: center;
    justify-content: center;
  }

  .front-shapes { position: absolute; inset: 0; width: 100%; height: 100%; }

  .brand {
    position: absolute;
    display: flex;
    align-items: center;
    font-family: "Raleway", Arial, sans-serif;
    font-weight: 700;
    letter-spacing: 1px;
  }
  .brand__mark { display: block; border-radius: 50%; }
  .brand--front { left: 62px; top: 95px; font-size: 52px; color: var(--navy); gap: 18px; }
  .brand--front .brand__mark { width: 34px; height: 34px; background: var(--teal); }
  .brand--back { position: static; font-size: 70px; color: var(--text-light); gap: 24px; }
  .brand--back .brand__mark { width: 44px; height: 44px; background: var(--lime); }

  .holder {
    position: absolute;
    left: 62px;
    top: 318px;
    font-family: "Lato", Arial, sans-serif;
  }
  .holder__name {
    font-weight: 700;
    font-size: 36px;
    letter-spacing: 1.5px;
    line-height: 44px;
    color: var(--navy);
  }
  .holder__title {
    margin-top: 6px;
    font-weight: 400;
    font-size: 19px;
    letter-spacing: 2px;
    line-height: 26px;
    color: var(--teal);
    text-transform: uppercase;
  }

  .contact {
    position: absolute;
    right: 78px;
    top: 263px;
    list-style: none;
    font-family: "Lato", Arial, sans-serif;
    font-size: 22px;
    color: var(--text-light);
    text-align: right;
  }
  .contact__row {
    display: flex;
    justify-content: flex-end;
    align-items: flex-start;
    gap: 16px;
    line-height: 34px;
  }
  .contact__row--address { margin-top: 18px; line-height: 30px; }
  .contact__icon { width: 14px; height: 14px; margin-top: 10px; flex: none; }
</style>
</head>
<body>
<main class="canvas">

  <section class="card card--front" aria-label="Business card front">
    <svg class="front-shapes" viewBox="0 0 701 410" preserveAspectRatio="none" aria-hidden="true">
      <defs>
        <linearGradient id="panel-gradient" x1="0" y1="0" x2="1" y2="0">
          <stop offset="0" stop-color="#00bba5"/>
          <stop offset="0.55" stop-color="#0094d4"/>
          <stop offset="1" stop-color="#0054aa"/>
        </linearGradient>
      </defs>
      <polygon class="wedge" points="412,0 484,0 451,140" fill="#c6efe9"/>
      <polygon class="gradient-panel" points="553,0 701,0 701,410 266,410 451,140" fill="url(#panel-gradient)"/>
      <polygon class="band" points="412,0 470,0 701,205 701,268" fill="#0054aa"/>
      <line class="accent-line" x1="431" y1="150" x2="246" y2="410" stroke="#00ab8e" stroke-width="2.5"/>
    </svg>

    <div class="brand brand--front">
      <span class="brand__mark"></span>
      <span class="brand__name">VERODEX</span>
    </div>

    <div class="holder">
      <h1 class="holder__name">DANA WHITLOW</h1>
      <p class="holder__title">Carbon Markets Director</p>
    </div>

    <ul class="contact">
      <li class="contact__row">
        <span>(700) 555-0142</span>
        <svg class="contact__icon" viewBox="0 0 14 14" aria-hidden="true"><path d="M3 1l2.5 3-1.5 1.5c.8 1.8 2.2 3.2 4 4L9.5 8l3 2.5-1.5 2.5C6 13 1 8 1 2.5z" fill="#fff"/></svg>
      </li>
      <li class="contact__row">
        <span>dana@verodex.com</span>
        <svg class="contact__icon" viewBox="0 0 14 14" aria-hidden="true"><rect x="1" y="3" width="12" height="8" fill="#fff"/><path d="M1 3l6 5 6-5" fill="none" stroke="#0677ba" stroke-width="1"/></svg>
      </li>
      <li class="contact__row">
        <span>www.verodex.com</span>
        <svg class="contact__icon" viewBox="0 0 14 14" aria-hidden="true"><circle cx="7" cy="7" r="6" fill="#fff"/><path d="M1 7h12M7 1c-2.5 3-2.5 9 0 12M7 1c2.5 3 2.5 9 0 12" fill="none" stroke="#0677ba" stroke-width="1"/></svg>
      </li>
      <li class="contact__row contact__row--address">
        <span>48 Alder Lane<br>Brookfield, NY 0000</span>
        <svg class="contact__icon" viewBox="0 0 14 14" aria-hidden="true"><path d="M7 1a4 4 0 0 1 4 4c0 3-4 7-4 7S3 8 3 5a4 4 0 0 1 4-4z" fill="#fff"/><circle cx="7" cy="5" r="1.5" fill="#0677ba"/></svg>
      </li>
    </ul>
  </section>

  <section class="card card--back" aria-label="Business card back">
    <div class="brand brand--back">
      <span class="brand__mark"></span>
      <span class="brand__name">VERODEX</span>
    </div>
  </section>

</main>
</body>
</html>
```